Corvel Lease Homes
will not have subtitle
Corvel Lease Homes -
Creative Brief
Simple
Paul Venner, Tessa Venner
PO Box 58211 20415 #7 Rd Surrey, BC V2T 5K9
info@corvelholdings.ca
www.corvelholdings.ca
On front- white background with small logo and our contact info. Paul's # is 604.555.0187, mine is the other. would like all the colors to be the same as logo and info in blue. Back- blue background with large logo. I would also be interested in simply seeing what you all come up with as you know what looks best-so feel free to do something different than what I said and we'll go from there. Thank you.

```html
<!DOCTYPE html>
<html lang="en">
<head>
<meta charset="utf-8">
<title>Corvel Lease Homes – Business Cards</title>
<link rel="stylesheet" href="https://fonts.googleapis.com/css2?family=Cinzel:wght@400;600&family=Cormorant+Garamond:wght@500;600&display=swap">
<style>
  :root {
    --backdrop: #ece8e2;
    --card-white: #ffffff;
    --card-edge: #e4e8ec;
    --brand-blue: #1b74b8;
    --deep-blue: #0d4f86;
    --bright-blue: #2f9be0;
    --ink-blue: #1d5f99;
    --rule-grey: #b9c3cc;
  }
  * { box-sizing: border-box; margin: 0; padding: 0; }
  html, body {
    width: 1200px; height: 737px; overflow: hidden;
    background: var(--backdrop);
  }
  .canvas { position: relative; width: 1200px; height: 737px; }

  .card {
    position: absolute;
    width: 420px; height: 240px;
    border-radius: 12px;
    overflow: hidden;
    box-shadow: 0 10px 22px rgba(40, 30, 20, 0.28);
  }
  .card--contact { left: 110px; top: 180px; background: var(--card-white); }
  .card--reverse { left: 680px; top: 150px;
    background: linear-gradient(135deg, var(--bright-blue) 0%, var(--brand-blue) 45%, var(--deep-blue) 100%); }
  .card--plain { left: 350px; top: 450px; background: var(--card-white); }

  .wordmark {
    font-family: "Cinzel", serif;
    font-weight: 600;
    color: var(--brand-blue);
    text-align: center;
    line-height: 1.05;
  }
  .wordmark__line { display: block; }
  .wordmark__line--main { letter-spacing: 0.02em; }

  /* contact side */
  .card--contact .wordmark { position: absolute; left: 18px; top: 78px; width: 180px; font-size: 26px; }
  .card--contact .wordmark__line--sub { font-size: 19px; margin-top: 4px; }
  .divider { position: absolute; left: 208px; top: 34px; width: 1px; height: 150px; background: var(--rule-grey); }
  .contact { position: absolute; left: 222px; top: 34px; width: 190px; color: var(--ink-blue);
    font-family: "Cormorant Garamond", serif; font-weight: 600; }
  .contact__name { font-family: "Cinzel", serif; font-weight: 400; font-size: 16px; letter-spacing: 0.02em; }
  .contact__role { font-size: 9px; letter-spacing: 0.08em; text-transform: uppercase; margin-bottom: 10px; color: var(--brand-blue); }
  .contact__line { font-size: 9.5px; line-height: 1.35; }
  .contact__gap { height: 12px; }
  .card__band { position: absolute; left: 0; right: 0; bottom: 0; height: 16px;
    background: linear-gradient(90deg, var(--bright-blue), var(--deep-blue)); }

  /* reverse side */
  .card--reverse .wordmark { position: absolute; left: 0; right: 0; top: 62px; color: var(--card-white); font-size: 40px; }
  .card--reverse .wordmark__line--sub { font-size: 28px; margin-top: 4px; }
  .url { font-family: "Cinzel", serif; font-weight: 600; font-size: 14px; letter-spacing: 0.02em; }
  .card--reverse .url { position: absolute; left: 38px; bottom: 26px; color: var(--card-white); }

  /* plain front */
  .card--plain .wordmark { position: absolute; left: 0; right: 0; top: 62px; font-size: 36px; }
  .card--plain .wordmark__line--sub { font-size: 25px; margin-top: 4px; }
  .card--plain .url { position: absolute; left: 0; right: 0; bottom: 30px; text-align: center; color: var(--ink-blue); }
</style>
</head>
<body>
<main class="canvas">

  <section class="card card--contact" aria-label="Front of card with contact details">
    <div class="wordmark">
      <span class="wordmark__line wordmark__line--main">Corvel</span>
      <span class="wordmark__line wordmark__line--sub">Lease Homes</span>
    </div>
    <div class="divider"></div>
    <div class="contact">
      <p class="contact__name">Paul Venner</p>
      <p class="contact__role">Owner</p>
      <p class="contact__name">Tessa Venner</p>
      <p class="contact__role">Owner</p>
      <p class="contact__line">PO Box 58211 20415 #7 Rd</p>
      <p class="contact__line">Surrey, BC V2T 5K9</p>
      <p class="contact__line">Paul: 604.555.0187 · Tessa: 604.555.0342</p>
      <div class="contact__gap"></div>
      <p class="contact__line">info@corvelholdings.ca</p>
      <p class="contact__line">www.corvelholdings.ca</p>
    </div>
    <div class="card__band"></div>
  </section>

  <section class="card card--reverse" aria-label="Back of card">
    <div class="wordmark">
      <span class="wordmark__line wordmark__line--main">Corvel</span>
      <span class="wordmark__line wordmark__line--sub">Lease Homes</span>
    </div>
    <p class="url">www.corvelholdings.ca</p>
  </section>

  <section class="card card--plain" aria-label="Alternate white back of card">
    <div class="wordmark">
      <span class="wordmark__line wordmark__line--main">Corvel</span>
      <span class="wordmark__line wordmark__line--sub">Lease Homes</span>
    </div>
    <p class="url">www.corvelholdings.ca</p>
  </section>

</main>
</body>
</html>
```